'Cradle Ahead' promotional brochure

We have designed a 6 week program to educate impending first-time parents about the things they need to know to survive the first 6 months. Sessions delivered by general practitioner/family doctor, dietician, physiotherapist, speech pathologist and psychologist. Our promotional blurb is: 'A comprehensive education program for first-time parents-to-be, delivered over 6 weeks by health professionals in your community, about everything you need to know to look after your baby (and yourself!) in the first 6 months'. I now want to put together a promotional brochure to be distributed to those couples who express an interest which will provide further details of what will be delivered in the course.
Updates
In terms of layout, I envisaged a double sided A4 size, foldable into 3 sections, but very happy to be guided on this.
Target Market(s)
To appeal to a young, well educated demographic. First time parents couples.
Industry/Entity Type
Medical
Font styles to use
Other font styles liked:
- Playfair Display
Requirements
Must have
- Playfair display font to be consistent with our logo (attached). Logo also included please. Some consistency with colours of logo please.
Nice to have
- I am a doctor, and have no creative genes! But prefer a clean and professional appearance overall. Not too cluttered in overall appearance.
Should not have
- No cheesy pictures of babies.

```html
<!DOCTYPE html>
<html lang="en">
<head>
<meta charset="utf-8">
<title>Cradle Ahead – Brochure</title>
<link href="https://fonts.googleapis.com/css2?family=Playfair+Display:wght@400;700&display=swap" rel="stylesheet">
<style>
  :root{
    --green:#8cc63f;
    --green-dark:#6aa621;
    --grey:#6d6e70;
    --grey-dark:#58595b;
    --paper:#f4f4f4;
    --white:#ffffff;
    --bg:#a9cbe3;
    --ink:#4d4d4f;
  }
  *{box-sizing:border-box;margin:0;padding:0}
  html,body{width:1200px;height:1200px;overflow:hidden}
  body{background:var(--bg);font-family:"Playfair Display",Georgia,serif;color:var(--ink)}
  .spread{position:absolute;left:30px;width:1140px;height:560px;display:flex;background:var(--paper);box-shadow:0 6px 18px rgba(0,0,0,.18)}
  .spread--inside{top:20px}
  .spread--outside{top:620px}
  .panel{position:relative;width:380px;height:560px;overflow:hidden;border-right:1px solid #ddd}
  .panel:last-child{border-right:none}
  .panel::after{content:"";position:absolute;left:0;right:0;bottom:0;height:22px;background:var(--grey)}
  .block{position:absolute;left:0;right:0;padding:16px 26px;overflow:hidden}
  .block--grey{background:var(--grey);color:var(--white)}
  .block--green{background:var(--green);color:var(--white)}
  .block--white{background:var(--paper);color:var(--green-dark)}
  .photo{position:absolute;left:0;right:0}
  .photo--hands{background:linear-gradient(135deg,#f3eeee,#d9b8a8 55%,#b98c7c)}
  .photo--consult{background:linear-gradient(135deg,#e9ece9,#c9b7a4 50%,#7d6a5c)}
  .photo--nurse{background:linear-gradient(135deg,#e7edf2,#d8c39a 45%,#a9b4bd)}
  .photo--clinic{background:linear-gradient(135deg,#eef1f4,#d7c4b6 50%,#8c9aae)}
  .stripes{position:absolute;top:0;left:0;right:0;height:64px;background:var(--paper)}
  .stripe{position:absolute;left:0;right:0;height:14px;background:var(--green)}
  .stripe--thin{height:6px;background:var(--grey)}
  .week{font-size:16px;display:inline-block;border-bottom:2px solid currentColor;padding-bottom:1px;margin-bottom:8px}
  .session{font-size:12.5px;display:flex;align-items:center;gap:6px;margin-top:8px}
  .session::before{content:"";width:6px;height:6px;border-radius:50%;background:currentColor}
  .block--grey .session::before,.block--white .session::before{background:var(--green)}
  p{font-size:10.5px;line-height:1.35}
  ul{list-style:none;margin-top:4px}
  li{font-size:10.5px;line-height:1.32;padding-left:12px;position:relative}
  li::before{content:"";position:absolute;left:0;top:5px;width:6px;height:6px;border-radius:50%;background:var(--green)}
  .block--green li::before{background:var(--white)}
  .brand{display:flex;align-items:center;gap:10px;justify-content:center}
  .brand__mark{width:14px;height:14px;border-radius:50%;background:var(--grey-dark)}
  .brand__name{font-size:20px;color:var(--grey-dark)}
  .program-title{margin-top:18px;text-align:center;font-size:30px;color:var(--grey-dark)}
  .blurb{position:absolute;left:0;right:22px;top:408px;height:122px;background:var(--green);border-radius:0 22px 22px 0;color:var(--white);font-size:12.5px;line-height:1.36;text-align:center;padding:10px 16px}
  .contact{text-align:center;font-size:30px;margin-top:40px}
  .contact span{border-bottom:2px solid var(--white);padding:0 6px 2px}
</style>
</head>
<body>

<section class="spread spread--inside">
  <div class="panel">
    <div class="photo photo--hands" style="top:0;height:272px" role="img" aria-label="Close-up photo of a baby's hand holding a parent's finger"></div>
    <div style="position:absolute;top:300px;left:0;right:0">
      <div class="brand"><div class="brand__mark"></div><div class="brand__name">Northgate Family Clinic</div></div>
      <div class="program-title">Cradle Ahead</div>
    </div>
    <div class="blurb">A comprehensive education program for first-time parents-to-be, delivered over 6 weeks by health professionals in your community, about everything you need to know to look after your baby (and yourself!) in the first 6 months</div>
  </div>

  <div class="panel">
    <div class="stripes">
      <div class="stripe" style="top:12px"></div>
      <div class="stripe stripe--thin" style="top:34px"></div>
      <div class="stripe" style="top:46px"></div>
    </div>
    <div class="block block--grey" style="top:64px;height:236px;padding:18px 36px">
      <div class="week">Week 1</div>
      <p>GP Dr Helen Marsh will share information for Mum's own health after delivery.</p>
      <p style="margin-top:12px">Topics include:</p>
      <ul>
        <li>Vaccinations in pregnancy</li>
        <li>Bleeding, bladder and bowel after delivery</li>
        <li>Breastfeeding, engorgement and mastitis</li>
        <li>Bottle feeding</li>
        <li>Post-natal anxiety &amp; depression</li>
        <li>Intimacy and contraception</li>
      </ul>
    </div>
    <div class="block block--white" style="top:300px;height:238px;padding:14px 36px">
      <div class="week">Week 2</div>
      <div class="session" style="margin-top:0">Session 1</div>
      <p>Clinical Psychologist Dr Anna Lindqvist will discuss changes in relationships as couples become parents, gender roles in parenting and post-natal depression.</p>
      <div class="session">Session 2</div>
      <p>Physiotherapist Tessa Moore will present advice for Mums regarding exercise during and after pregnancy, looking after the pelvic floor, and abdominal muscle separation management. She will also provide advice for promoting babies' neck strength, minimising the risk of flat spots on the head and encouraging gross motor skills in the first 6 months.</p>
    </div>
  </div>

  <div class="panel">
    <div class="stripes">
      <div class="stripe" style="top:12px"></div>
      <div class="stripe stripe--thin" style="top:34px"></div>
      <div class="stripe" style="top:46px"></div>
    </div>
    <div class="photo photo--consult" style="top:64px;height:236px" role="img" aria-label="Photo of a doctor reviewing notes with a young woman"></div>
    <div class="block block--grey" style="top:300px;height:238px;padding:12px 16px">
      <div class="week">Week 3</div>
      <div class="session" style="margin-top:0">Session 1</div>
      <p style="font-size:9.5px">Dietician Ruth Calder provides advice for Mums regarding healthy eating during pregnancy and lactation, normal weight gain during pregnancy and realistic weight loss after. She will also discuss the evidence regarding breastfeeding vs bottle-feeding, normal infant weight gain and introducing solids (including those with potential for allergy).</p>
      <div class="session">Session 2</div>
      <p style="font-size:9.5px">Paediatric Speech Pathologist Jane Hollis will share information about latching and breast-feeding troubles &amp; tongue tie, advice about dummies and finger sucking, introducing solids &amp; feeding (including 'pouch food'), encouraging language development and current evidence about electronic devices impacting language development.</p>
    </div>
  </div>
</section>

<section class="spread spread--outside">
  <div class="panel">
    <div class="stripes">
      <div class="stripe" style="top:12px"></div>
      <div class="stripe stripe--thin" style="top:34px"></div>
      <div class="stripe" style="top:46px"></div>
    </div>
    <div class="photo photo--nurse" style="top:64px;height:196px" role="img" aria-label="Photo of a smiling nurse talking with a young mother"></div>
    <div class="block block--green" style="top:260px;height:180px;padding:10px 30px">
      <div class="week" style="margin-bottom:4px">Week 4</div>
      <p>GP Dr Helen Marsh will share advice about your babies' health in the first 6 months, including:</p>
      <ul>
        <li>Skin of newborns</li><li>Sleeping</li><li>Crying</li><li>Immunisations</li>
        <li>Fevers and infections</li><li>Diarrhoea and constipation</li><li>Teething</li>
        <li>Understanding a baby's signals</li>
      </ul>
    </div>
    <div class="block block--white" style="top:440px;height:98px;padding:8px 30px">
      <div class="week" style="margin-bottom:2px">Week 5</div>
      <div class="session" style="margin-top:0">Session 1</div>
      <p style="font-size:9.5px;line-height:1.28">Clinical Psychologist Dr Anna Lindqvist will share information about bonding &amp; attachment with your baby, social &amp; emotional development and separation anxiety.</p>
    </div>
  </div>

  <div class="panel">
    <div class="block block--grey" style="top:0;height:290px">
      <div class="contact"><span>CONTACT US</span></div>
    </div>
    <div style="position:absolute;top:360px;left:0;right:0">
      <div class="brand"><div class="brand__mark"></div><div class="brand__name">Northgate Family Clinic</div></div>
      <div class="program-title" style="font-size:32px">Cradle Ahead</div>
    </div>
  </div>

  <div class="panel">
    <div class="block block--green" style="top:0;height:290px;padding:44px 30px">
      <div class="week">Week 6</div>
      <div class="session" style="margin-top:4px">Session 1</div>
      <p>Secret Men's Business – a men-only session including beers with a new father for frank discussion about the road ahead. Mums will do a shopping excursion with the GP &amp; Dietician to Greenway Market to look at baby products and food – the good and the bad!</p>
      <div class="session" style="margin-top:12px">Session 2</div>
      <p>Program review, reflection and evaluation and future session planning when baby is 6 months of age.</p>
    </div>
    <div class="photo photo--clinic" style="top:290px;height:248px" role="img" aria-label="Photo of a doctor explaining a chart to a young couple"></div>
  </div>
</section>

</body>
</html>
```